Personal Trainer Business Card Design and Logo

I am a Personal Trainer and passionate in helping obese kids loose weight, I would love a business card design for my business called LORK Fitness.
LORK Ftiness stands for Lively Origami Running Kicks, I would like the business card to be bright and appealing to the kids as well as the parents.
I would also love a logo designs witch is simple but affective.

Things I would like in the business card
- Kids playing and being happy (no cartoon characters)
- The card should be bright and colourful
- My name, Bartholomew Van Rijk Personal Trainer
- Contact number 0472618059
- Email address lorkfitness@mailzorp.com

Things I would like in the logo
-colourful design which incorporate kids
- your creative logo

thanks for all your entries
kind regards Bart

loving all the designs, you are all so talented.

could you please read the updated brief

kind regards

Bart

Reason: Loving the designs, but needs more modification kind reagrds Bart

Target Market(s)

Kids and Parents

Industry/Entity Type

Business

Contact Information for Business Card

LORK Fitness for kids

Lively Origami Running Kicks

Bart Van Rijk Personal Trainer
0472618059

Requirements
Must have
• Kids laughing and happy, lork fitness logo, Bart Van Rijk Personal Trainer, 0472618059,lorkfitness@mailzorp.com, colourful and bright.
Nice to have
• pulsewell council tick

```html
<!DOCTYPE html>
<html lang="en">
<head>
<meta charset="utf-8">
<title>LORK Fitness for kids – Business Card</title>
<link rel="stylesheet" href="https://fonts.googleapis.com/css2?family=Open+Sans:wght@400;600;700&display=swap">
<style>
  :root {
    --page-bg: #e9e5df;
    --card-white: #ffffff;
    --green-light: #b4dc4a;
    --green-mid: #8cc63f;
    --green-deep: #6aad2a;
    --brand-green: #7dbb32;
    --accent-orange: #f39a1e;
    --accent-blue: #1b8fd2;
    --text-dark: #2f3a22;
    --text-white: #ffffff;
    --photo-warm: #e8d3bd;
    --photo-cool: #cfe3ee;
  }
  * { box-sizing: border-box; margin: 0; padding: 0; }
  html, body {
    width: 1200px; height: 800px; overflow: hidden;
    background: var(--page-bg);
    font-family: "Open Sans", Arial, sans-serif;
  }
  .canvas { position: relative; width: 1200px; height: 800px; }

  .card {
    position: absolute; top: 245px;
    width: 540px; height: 310px;
    border-radius: 16px; overflow: hidden;
    box-shadow: 0 10px 26px rgba(60, 50, 40, .22);
  }

  /* Back of card */
  .card-back {
    left: 45px;
    background: linear-gradient(160deg, var(--green-light) 0%, var(--green-mid) 55%, var(--green-deep) 100%);
  }
  .card-back .back-title {
    position: absolute; right: 44px; top: 92px;
    text-align: right; color: var(--text-white);
  }
  .back-title .brand-name { font-size: 25px; font-weight: 700; }
  .back-title .tagline { font-size: 15px; font-weight: 400; margin-top: 2px; }

  /* Front of card */
  .card-front { left: 615px; background: var(--green-mid); }
  .front-top {
    position: absolute; left: 0; top: 0; width: 100%; height: 124px;
    background: var(--card-white);
  }
  .blue-band {
    position: absolute; left: 0; top: 124px; width: 100%; height: 7px;
    background: var(--accent-blue);
  }
  .front-bottom {
    position: absolute; left: 0; top: 131px; width: 100%; height: 179px;
    background: linear-gradient(180deg, var(--green-light) 0%, var(--green-mid) 100%);
  }
  .kids-photo {
    position: absolute; right: 14px; top: 6px; width: 250px; height: 114px;
    border-radius: 6px;
    background: linear-gradient(120deg, var(--photo-warm), var(--photo-cool));
  }
  .brand-block { position: absolute; left: 26px; top: 40px; }
  .brand-line { display: flex; align-items: center; gap: 8px; }
  .brand-dot {
    width: 14px; height: 14px; border-radius: 50%;
    background: var(--accent-orange);
  }
  .brand-block .brand-name {
    font-size: 20px; font-weight: 700; color: var(--brand-green);
  }
  .brand-block .tagline {
    font-size: 13px; color: var(--accent-orange); margin: 3px 0 0 22px;
  }

  .contact-block { position: absolute; left: 26px; top: 148px; }
  .trainer-name {
    font-size: 18px; font-weight: 700; color: var(--accent-blue);
    letter-spacing: .3px;
  }
  .trainer-role { font-size: 14px; color: var(--text-dark); margin-bottom: 8px; }
  .contact-list { list-style: none; }
  .contact-list li {
    display: flex; align-items: center; gap: 8px;
    font-size: 14px; color: var(--text-dark); line-height: 23px;
  }
  .contact-icon {
    width: 15px; height: 15px; border-radius: 3px;
    background: var(--accent-blue);
    display: flex; align-items: center; justify-content: center;
  }
  .contact-icon svg { width: 11px; height: 11px; }
</style>
</head>
<body>
<main class="canvas">

  <section class="card card-back" aria-label="Business card back">
    <div class="back-title">
      <div class="brand-name">LORK Fitness for kids</div>
      <div class="tagline">Lively Origami Running Kicks</div>
    </div>
  </section>

  <section class="card card-front" aria-label="Business card front">
    <div class="front-top"></div>
    <div class="blue-band"></div>
    <div class="front-bottom"></div>

    <div class="kids-photo" role="img" aria-label="Photo of four happy kids jumping in the air"></div>

    <div class="brand-block">
      <div class="brand-line">
        <span class="brand-dot"></span>
        <span class="brand-name">LORK Fitness for kids</span>
      </div>
      <div class="tagline">Lively Origami Running Kicks</div>
    </div>

    <div class="contact-block">
      <div class="trainer-name">BART VAN RIJK</div>
      <div class="trainer-role">Personal Trainer</div>
      <ul class="contact-list">
        <li>
          <span class="contact-icon">
            <svg viewBox="0 0 12 12"><path d="M3 1.5h2l.8 2-1.2.9a6 6 0 0 0 3 3l.9-1.2 2 .8v2A1 1 0 0 1 9.5 10 8.5 8.5 0 0 1 2 2.5a1 1 0 0 1 1-1z" fill="#fff"/></svg>
          </span>
          0472 618 059
        </li>
        <li>
          <span class="contact-icon">
            <svg viewBox="0 0 12 12"><rect x="1.5" y="3" width="9" height="6" fill="none" stroke="#fff" stroke-width="1.2"/><path d="M1.5 3 6 6.5 10.5 3" fill="none" stroke="#fff" stroke-width="1.2"/></svg>
          </span>
          lorkfitness@mailzorp.com
        </li>
        <li>
          <span class="contact-icon">
            <svg viewBox="0 0 12 12"><circle cx="6" cy="6" r="4.3" fill="none" stroke="#fff" stroke-width="1.1"/><path d="M1.7 6h8.6M6 1.7c-2 2.4-2 6.2 0 8.6M6 1.7c2 2.4 2 6.2 0 8.6" fill="none" stroke="#fff" stroke-width="1"/></svg>
          </span>
          lorkfitnesskids.net
        </li>
      </ul>
    </div>
  </section>

</main>
</body>
</html>
```